Redesign business cards

We have a new logo and I am not that happy with the layout of our existing card and looking for a change. Font is a bit small and the green can be hard to read. Logo may need a tidy up as the copy I have is not that hi-res too so require you to produce a hi-res version of the logo for us too. There will be three individual business cards to produce with just the names and phone numbers being different. Address will change too, but use what you see on the card for now.

Industry/Entity Type

Business

Requirements
Nice to have
• You could consider a redesign to the new logo, just not too radical. We like the blue and green hexagons as we feel that they are representative of oil industry that we are in.

```html
<!DOCTYPE html>
<html lang="en">
<head>
<meta charset="utf-8">
<title>Corvane Fuel Services – Business Cards</title>
<link rel="stylesheet" href="https://fonts.googleapis.com/css2?family=Source+Sans+3:wght@400;600;700&display=swap">
<style>
  :root {
    --bg: #3b3b3b;
    --card: #ffffff;
    --blue: #29a8e0;
    --sky: #4bc6ec;
    --pale-blue: #7ccbf0;
    --green: #8cc63f;
    --pale-green: #c4e0a0;
    --ink: #1e1e1e;
    --font: "Source Sans 3", "Myriad Pro", Arial, sans-serif;
  }
  * { box-sizing: border-box; margin: 0; padding: 0; }
  html, body { width: 1200px; height: 750px; overflow: hidden; }
  body { background: var(--bg); font-family: var(--font); position: relative; }

  .card {
    position: absolute;
    top: 210px;
    width: 511px;
    height: 293px;
    background: var(--card);
    overflow: hidden;
  }
  .card--front { left: 78px; }
  .card--back { left: 609px; }

  .hex-field {
    position: absolute;
    background: linear-gradient(135deg, var(--sky) 0%, var(--blue) 30%, var(--green) 55%, var(--pale-blue) 100%);
  }
  .card--front .hex-field {
    left: 0; top: 0;
    width: 218px; height: 228px;
    clip-path: polygon(0 0, 100% 0, 100% 55%, 70% 100%, 0 100%);
  }
  .card--back .hex-field {
    right: 0; bottom: 0;
    width: 132px; height: 122px;
    clip-path: polygon(30% 0, 100% 0, 100% 100%, 0 100%, 0 30%);
  }

  .wordmark {
    position: absolute;
    font-family: var(--font);
    font-weight: 700;
    color: var(--blue);
    line-height: 1.05;
  }
  .wordmark__sub { display: block; font-size: 0.48em; }
  .card--front .wordmark { left: 172px; top: 196px; font-size: 46px; }
  .card--back .wordmark { left: 26px; top: 74px; font-size: 40px; }

  .person {
    position: absolute;
    right: 25px; top: 44px;
    text-align: right;
    color: var(--ink);
  }
  .person__name { font-size: 21px; font-weight: 400; }
  .person__credential { font-size: 11px; font-weight: 600; margin-top: 1px; }

  .contact {
    position: absolute;
    left: 24px; top: 165px;
    list-style: none;
    font-size: 15.5px;
    line-height: 19px;
  }
  .contact__item { display: flex; align-items: flex-start; gap: 16px; color: var(--ink); }
  .contact__item--address { color: var(--blue); margin-top: 6px; }
  .contact__icon { width: 16px; height: 16px; flex: none; margin-top: 2px; fill: var(--sky); }
</style>
</head>
<body>

<section class="card card--front" aria-label="Card front">
  <div class="hex-field" role="img" aria-label="Blue and green hexagon pattern"></div>
  <div class="wordmark">Corvane<span class="wordmark__sub">Fuel Services</span></div>
</section>

<section class="card card--back" aria-label="Card back">
  <div class="wordmark">Corvane<span class="wordmark__sub">Fuel Services</span></div>

  <div class="person">
    <p class="person__name">Ellis Navarro</p>
    <p class="person__credential">NZCE (Mech) P&amp;P</p>
  </div>

  <ul class="contact">
    <li class="contact__item">
      <svg class="contact__icon" viewBox="0 0 16 16"><path d="M2 6c0-2 3-3.5 6-3.5S14 4 14 6v1.5h-3V6H5v1.5H2z"/><rect x="3" y="9" width="10" height="4.5" rx="1"/></svg>
      <span>+61 4 5550 1842</span>
    </li>
    <li class="contact__item">
      <svg class="contact__icon" viewBox="0 0 16 16"><path d="M1.5 4h13v8h-13z M2.5 4.5 8 9l5.5-4.5" stroke="#fff" stroke-width="1"/></svg>
      <span>ellis@corvanefuel.com</span>
    </li>
    <li class="contact__item">
      <svg class="contact__icon" viewBox="0 0 16 16" fill="none" stroke="#4bc6ec" stroke-width="1.2"><circle cx="8" cy="8" r="6.5"/><ellipse cx="8" cy="8" rx="2.8" ry="6.5"/><path d="M1.5 8h13M2.5 4.8h11M2.5 11.2h11"/></svg>
      <span>www.corvanefuel.com</span>
    </li>
    <li class="contact__item contact__item--address">
      <svg class="contact__icon" viewBox="0 0 16 16"><path d="M8 1a5 5 0 0 0-5 5c0 3.5 5 9 5 9s5-5.5 5-9a5 5 0 0 0-5-5zm0 7a2 2 0 1 1 0-4 2 2 0 0 1 0 4z"/></svg>
      <span>Corvane Fuel Services 214<br>Harlow Street, PO Box 5170<br>Brindale Queensland 4109</span>
    </li>
  </ul>

  <div class="hex-field" role="img" aria-label="Blue and green hexagon pattern"></div>
</section>

</body>
</html>
```